Verdane Training Center
Golf Simulation & Character Education
Corporate
Milo Raskett
Chief Operations Officer
Brisby Center
North Charleston, SC
Milo@verdanetrainingcenter.com
verdanetrainingcenter.com
I would like for my logo design to be incorporated into the card design
logo full size of card on the back

```html
<!DOCTYPE html>
<html lang="en">
<head>
<meta charset="utf-8">
<title>Verdane Training Center – Business Card</title>
<link href="https://fonts.googleapis.com/css2?family=Open+Sans:wght@400;600;700;800&display=swap" rel="stylesheet">
<style>
  :root {
    --bg: #e9e6e1;
    --card: #ffffff;
    --green-dark: #1e7a34;
    --green: #3a9a3f;
    --green-light: #8cc63f;
    --ink: #1a1a1a;
    --text: #333333;
    --rule: #d6d6d6;
  }
  html, body {
    margin: 0;
    width: 1200px;
    height: 965px;
    overflow: hidden;
    background: var(--bg);
    font-family: "Open Sans", Arial, sans-serif;
  }
  .business-card {
    position: absolute;
    left: 100px;
    top: 149px;
    width: 1000px;
    height: 667px;
    border-radius: 36px;
    background: var(--card);
    overflow: hidden;
    box-shadow: 0 10px 30px rgba(0,0,0,0.18);
  }
  .card-shapes {
    position: absolute;
    inset: 0;
    width: 100%;
    height: 100%;
  }
  .brand-mark {
    position: absolute;
    left: 330px;
    top: 150px;
    width: 460px;
    text-align: center;
    color: var(--green-dark);
    font-weight: 800;
    line-height: 1.05;
  }
  .brand-mark .brand-name {
    display: block;
    font-size: 74px;
    letter-spacing: 1px;
  }
  .brand-mark .brand-sub {
    display: block;
    font-size: 30px;
    letter-spacing: 4px;
    text-transform: uppercase;
  }
  .identity {
    position: absolute;
    right: 530px;
    top: 355px;
    text-align: right;
  }
  .identity .person-name {
    margin: 0;
    font-size: 40px;
    font-weight: 700;
    color: var(--green-dark);
    line-height: 1.15;
  }
  .identity .person-title {
    margin: 0 0 22px;
    font-size: 25px;
    font-weight: 700;
    color: var(--ink);
  }
  .identity .address {
    margin: 0;
    font-size: 24px;
    color: var(--text);
    line-height: 1.35;
    font-style: normal;
  }
  .divider {
    position: absolute;
    left: 502px;
    top: 360px;
    width: 2px;
    height: 200px;
    background: var(--rule);
  }
  .contact-list {
    position: absolute;
    left: 535px;
    top: 372px;
    margin: 0;
    padding: 0;
    list-style: none;
  }
  .contact-list li {
    display: flex;
    align-items: center;
    height: 40px;
    font-size: 24px;
    color: var(--text);
  }
  .contact-list svg {
    width: 24px;
    height: 24px;
    margin-right: 16px;
    flex: none;
  }
</style>
</head>
<body>
  <div class="business-card">
    <svg class="card-shapes" viewBox="0 0 1000 667" preserveAspectRatio="none" aria-hidden="true">
      <defs>
        <linearGradient id="leftBand" x1="0" y1="0" x2="1" y2="0">
          <stop offset="0" stop-color="#1e7a34"/>
          <stop offset="1" stop-color="#6fb83b"/>
        </linearGradient>
        <linearGradient id="rightBand" x1="0" y1="0" x2="1" y2="0">
          <stop offset="0" stop-color="#6fb83b"/>
          <stop offset="1" stop-color="#1e7a34"/>
        </linearGradient>
      </defs>
      <!-- left swoosh -->
      <path d="M0 0 L40 0 Q0 420 250 667 L0 667 Z" fill="url(#leftBand)"/>
      <path d="M40 0 Q0 420 250 667 L275 667 Q30 420 58 0 Z" fill="#ffffff"/>
      <path d="M58 0 Q30 420 275 667" fill="none" stroke="#111" stroke-width="7"/>
      <!-- right swoosh -->
      <path d="M770 0 L1000 0 L1000 400 Q960 110 770 0 Z" fill="url(#rightBand)"/>
      <path d="M745 0 Q950 110 1000 410" fill="none" stroke="#111" stroke-width="7"/>
    </svg>

    <div class="brand-mark">
      <span class="brand-name">VERDANE</span>
      <span class="brand-sub">Training Center</span>
    </div>

    <div class="identity">
      <h1 class="person-name">Milo Raskett</h1>
      <p class="person-title">Chief Operations Officer</p>
      <address class="address">Brisby Center<br>North Charleston,&nbsp; SC 29410</address>
    </div>

    <div class="divider"></div>

    <ul class="contact-list">
      <li>
        <svg viewBox="0 0 24 24" aria-hidden="true"><rect x="7" y="2" width="10" height="20" rx="2" fill="#3a9a3f"/><rect x="9" y="5" width="6" height="9" fill="#fff"/></svg>
        843-555-0172
      </li>
      <li>
        <svg viewBox="0 0 24 24" aria-hidden="true"><circle cx="12" cy="12" r="4" fill="none" stroke="#3a9a3f" stroke-width="2.5"/><path d="M16 8 V14 Q16 17 19 16 Q22 14 21 10 A9 9 0 1 0 16 20" fill="none" stroke="#3a9a3f" stroke-width="2.5"/></svg>
        Milo@verdanetrainingcenter.com
      </li>
      <li>
        <svg viewBox="0 0 24 24" aria-hidden="true"><circle cx="12" cy="12" r="9" fill="none" stroke="#3a9a3f" stroke-width="2"/><ellipse cx="12" cy="12" rx="4" ry="9" fill="none" stroke="#3a9a3f" stroke-width="2"/><path d="M3 12 H21" stroke="#3a9a3f" stroke-width="2"/></svg>
        www.verdanetrainingcenter.com
      </li>
    </ul>
  </div>
</body>
</html>
```